Brisk Fixwell business card

I need business card for my business, I think you have all my details.six months ago I design with you car wrap design. We would like to design both side of the card. On front of card we would like logo , Name and our contact details.
At the back we are looking to mentioned our services.
The name will be:
Farzadullah Korimi
Managing Director
Ph:07843529176
Email:info@brisk-fixwell.com
Web:www.brisk-fixwell.com
So we have our logo, you don’t need to change the logo.
Please see the attachment.
Thanks

Target Market(s)

Home improvement

Industry/Entity Type

Home Improvement

Contact Information for Business Card

Company name: Brisk Fixwell
Name: Farzadullah Korimi
Position: Director
Ph:07843529176
Web: www.brisk-fixwell.com
Add: 42 Larkfield Crescent
Hounslow
TW3 9LB
SECOND PERSON
Nasirudin korimi
Position: Handyman
Ph: 07712 634508
Email: info@brisk-fixwell.com
Add: 18 Wrenmoor Park Lane
Hounslow
TW6 2QJ

```html
<!DOCTYPE html>
<html lang="en">
<head>
<meta charset="utf-8">
<title>Brisk Fixwell – Business Card</title>
<link rel="stylesheet" href="https://fonts.googleapis.com/css2?family=Roboto:wght@400;700&family=Roboto+Condensed:wght@700&display=swap">
<style>
  :root {
    --navy: #1c2a6b;
    --red: #e3202c;
    --ink: #3a3f4a;
    --paper: #ffffff;
    --bg: #e6e7ea;
    --grey-bar: #a3a6ab;
  }
  * { box-sizing: border-box; margin: 0; padding: 0; }
  html, body { width: 1200px; height: 1200px; overflow: hidden; }
  body {
    background: var(--bg);
    font-family: "Roboto", Arial, sans-serif;
    position: relative;
  }
  .card {
    position: absolute;
    left: 180px;
    width: 840px;
    height: 480px;
    box-shadow: 0 6px 18px rgba(0,0,0,0.18);
    overflow: hidden;
  }
  /* Back side */
  .card--back { top: 80px; background: var(--navy); color: var(--paper); }
  .card--back .brand {
    position: absolute; left: 0; right: 0; top: 170px;
    display: flex; align-items: center; justify-content: center; gap: 22px;
  }
  .card--back .brand-name {
    font-weight: 700; font-size: 64px; letter-spacing: 1px;
    color: var(--paper);
  }
  .card--back .brand-mark {
    width: 46px; height: 46px; border: 5px solid var(--paper);
  }
  .card--back .address {
    position: absolute; left: 0; right: 0; top: 280px;
    text-align: center; font-size: 22px; letter-spacing: 0.5px;
  }
  /* Front side */
  .card--front { top: 640px; background: var(--paper); }
  .card--front .brand-block {
    position: absolute; left: 70px; top: 196px; width: 360px;
  }
  .card--front .brand {
    display: flex; align-items: center; gap: 14px;
  }
  .card--front .brand-name {
    font-weight: 700; font-size: 44px; color: var(--navy); letter-spacing: 0.5px;
    white-space: nowrap;
  }
  .card--front .brand-mark {
    width: 30px; height: 30px; background: var(--navy); flex: none;
  }
  .brand-underbar {
    margin-top: 10px; width: 70px; height: 12px;
    background: var(--grey-bar);
  }
  .contact {
    position: absolute; left: 480px; top: 130px;
  }
  .person-name {
    font-family: "Roboto Condensed", "Arial Narrow", sans-serif;
    font-weight: 700; font-size: 27px; color: var(--navy); text-transform: uppercase;
  }
  .person-name .surname { color: var(--red); }
  .person-role { font-size: 17px; color: var(--ink); margin: 4px 0 22px; }
  .contact-list { list-style: none; }
  .contact-list li {
    display: flex; align-items: center; gap: 12px;
    font-size: 19px; color: var(--ink); margin-bottom: 12px;
  }
  .contact-icon { width: 20px; height: 20px; flex: none; }
</style>
</head>
<body>

<section class="card card--back" aria-label="Card back">
  <div class="brand">
    <span class="brand-name">Brisk Fixwell</span>
    <span class="brand-mark"></span>
  </div>
  <p class="address">42 Larkfield Crescent, Hounslow, TW3 9LB</p>
</section>

<section class="card card--front" aria-label="Card front">
  <div class="brand-block">
    <div class="brand">
      <span class="brand-name">Brisk Fixwell</span>
      <span class="brand-mark"></span>
    </div>
    <div class="brand-underbar"></div>
  </div>

  <div class="contact">
    <h1 class="person-name">Farzadullah <span class="surname">Korimi</span></h1>
    <p class="person-role">Director</p>
    <ul class="contact-list">
      <li>
        <svg class="contact-icon" viewBox="0 0 20 20" aria-hidden="true">
          <circle cx="10" cy="10" r="10" fill="var(--navy)"/>
          <path d="M6.5 5.5l2 0 1 2.5-1.3 1a6 6 0 0 0 2.8 2.8l1-1.3 2.5 1v2a1 1 0 0 1-1 1A8 8 0 0 1 5.5 6.5a1 1 0 0 1 1-1z" fill="#fff"/>
        </svg>
        07843529176
      </li>
      <li>
        <svg class="contact-icon" viewBox="0 0 20 20" aria-hidden="true">
          <circle cx="10" cy="10" r="10" fill="var(--navy)"/>
          <circle cx="10" cy="10" r="5" fill="none" stroke="#fff" stroke-width="1.3"/>
          <ellipse cx="10" cy="10" rx="2.2" ry="5" fill="none" stroke="#fff" stroke-width="1.1"/>
          <line x1="5" y1="10" x2="15" y2="10" stroke="#fff" stroke-width="1.1"/>
        </svg>
        www.brisk-fixwell.com
      </li>
      <li>
        <svg class="contact-icon" viewBox="0 0 20 20" aria-hidden="true">
          <circle cx="10" cy="10" r="10" fill="var(--navy)"/>
          <rect x="5" y="6.5" width="10" height="7" fill="none" stroke="#fff" stroke-width="1.3"/>
          <path d="M5 6.5l5 4 5-4" fill="none" stroke="#fff" stroke-width="1.3"/>
        </svg>
        info@brisk-fixwell.com
      </li>
    </ul>
  </div>
</section>

</body>
</html>
```